VESTRA電子書籍 表紙発注書

【依頼概要】

<サブタイトル>

小さな会社や個人事業でもできる!

<書籍タイトル>

数字が苦手な 店主のための
【看板づくり手帖】

※ターゲットの目にすぐ入る様に(小さな会社)(個人事業)(ネットに弱い)を目立つ様にお願いします。
※電子書籍なので表示される際の画像が小さいため、タイトルもできるだけ視認しやすい文字でお願いします。

<オビ部分>

ホームページを作る前に
必ずお読みください。

読者限定プレゼント付
●思わずポチッと押したくなる!
【段階別】キャッチコピーの作り方
●真似するだけでOK!
【ランディングページのテンプレート】

※プレゼントは目立つ様にお願いします。

<著者>

WEB集客のしくみ作りの専門家
森田 サキ

※著者似顔絵をどちらか使ってください。

<読者ターゲット層>
・40代~50代の、小規模企業の経営者・個人事業経営者・個人起業家

<イメージ>
・色の指定などはありません。
もし自分が起業する時なら、どんな表紙に目が止まるか考えてみていただけると嬉しいです。

・ビジネス書ではありますが、ターゲットはネットやパソコンに苦手意識を持っている経営者の方なので、また女性の起業家さんにも見て欲しいので、ちゃんとした雰囲気はありつつも、あまり硬くなく、自分でもできそうかなー、と思わせる様な雰囲気が出るといいなと思っています。
よろしくお願いいたします。

※著者似顔絵2点添付します。どちらかをお使いください。
※写真・イラスト素材購入の際は別途お支払いします。 その場合は、小サイズ画像で大丈夫です。

※参考資料として、まだ未完成ですが原稿を添付します。
パスワードがありますのでこちらで開いてください。

▶︎PDFを開く時のパスワード: demo1

《追記1》必ずご覧ください。
↓ ↓ ↓
書籍のタイトルとオビの文言をを変更しました。
申し訳ありませんが、こちらを必ずご確認ください。

(すでに提案をくださった方は、そのままのデザインで検討させていただきますので、再提出はしなくて大丈夫です。採用になった場合のみ変更のご依頼をさせていただきますが、その際は報酬をプラスさせていただきます※9/15日朝7時30分までに提案くださった方)

《変更内容》
<書籍タイトル>
帳簿が苦手な 店主のための
「街角で商売」

※ターゲットの目にすぐ入る様に(小さな会社)(個人事業)(ウェブに弱い)を目立つ様にお願いします。

<オビ部分>
※この本を読むまでは
ホームページは作らないでください。

▶︎参考本文(未完成)は新しい方(ファイル名:【原稿】こちらをご覧ください)
をご覧ください」
▶︎▶︎PDFファイルパスワード demo2
《追記2》
追記1にて一部変更をさせていただきましたが、
追記1の《変更内容》以外は最初の依頼内容通りなので、再度ご確認ください。

あと、少し気になったのですが、著者の似顔絵はメインビジュアルに使わなくて大丈夫です。名前の横にひっそりとつかう程度でいいかと思います。
もちろん、何か意図を持って使いたいという場合はご提案大歓迎です^ ^

▶︎必要な構成要素を再度まとめますね。
(読者ターゲットや希望デザインについては最初の依頼内容をご確認ください)
ーーーーーーーーーーーーーーーーーーー
<文字>
小さな会社や個人事業でもできる!

帳簿が苦手な 店主のための
「街角で商売」

※この本を読むまでは
ホームページは作らないでください。

読者限定プレゼント付
●思わずポチッと押したくなる!
【段階別 キャッチコピーの作り方】
●真似するだけでOK!
【ランディングページのテンプレート】

WEB集客のしくみ作りの専門家
森田 サキ

<画像>
著者似顔絵(メインビジュアルには使わなくていいいです)

※その他、写真・イラストの使用はお任せ

ーーーーーーーーーーーーーーーーーーー

こちらの説明不足のため誤解を招いてしまい、たいへん申し訳ございませんでした。

誰のための何の本ななのか、スマホでVestraを見た時でもはっきりわかるスッキリしたデザインがよかったです。また、こちらの要望通りに、ウェブが苦手な人や女性も、ついポチッと押してしまいそうなデザインでした。

選考には、20人ほどの方から意見をいただいたのですが、やはりはっきり文字が読み取れるものが人気が高かったです。
なるほどなぁ、と思ったのは、少しデザインの知識がある人(私を含め)と、とくにこだわりのない普通の人たちとでは、見る視点が違うのか、少し意見が別れました。読者目線がやはり大事ですね。

たくさんのご提案をいただき、本当にありがとうございました。

中には、さすがプロっぽいと思わせる作品や、手間をかけて作ってくださったと思われる作品もあり、本当にありがたく、また選考もかなり迷いました。

提案してくださった皆様、本当にありがとうございました。

```html
<!DOCTYPE html>
<html lang="ja">
<head>
<meta charset="utf-8">
<title>帳簿が苦手な 店主のための「街角で商売」</title>
<link rel="stylesheet" href="https://fonts.googleapis.com/css2?family=Noto+Sans+JP:wght@500;700;900&family=Noto+Serif+JP:wght@700;900&display=swap">
<style>
  :root {
    --paper: #f3f3f0;
    --ink: #1c1c1c;
    --accent: #e5561d;
    --ribbon: #c7272a;
    --gold-light: #f6de8a;
    --gold-dark: #c79a2e;
    --drop: #5aa9e0;
    --rule: #9a9a9a;
    --portrait-top: #c98a5a;
    --portrait-bottom: #2b3552;
  }
  html, body { margin: 0; padding: 0; overflow: hidden; }
  body { width: 750px; height: 1200px; }
  .cover {
    position: relative;
    width: 750px; height: 1200px;
    background: var(--paper);
    font-family: "Noto Sans JP", sans-serif;
    color: var(--ink);
    overflow: hidden;
  }
  .title { position: absolute; left: 0; right: 0; text-align: center; font-weight: 900; margin: 0; line-height: 1.2; white-space: nowrap; }
  .title-line1 { top: 70px; font-size: 76px; }
  .title-line1 .emph { font-size: 90px; }
  .title-line2 { top: 205px; font-size: 86px; }
  .title-main { top: 335px; font-size: 90px; }
  .sweat { position: absolute; left: 668px; top: 22px; }

  .subtitle {
    position: absolute; left: 215px; top: 505px; width: 500px;
    font-weight: 900; font-size: 36px; line-height: 56px;
  }
  .subtitle p { margin: 0; border-bottom: 2px solid var(--rule); padding: 6px 0 6px 35px; white-space: nowrap; }
  .subtitle .key { color: var(--accent); font-size: 44px; }

  .portrait {
    position: absolute; left: 505px; top: 668px; width: 195px; height: 262px;
    border-radius: 98px 98px 16px 16px;
    background: linear-gradient(180deg, var(--portrait-top), var(--portrait-bottom));
  }

  .badge { position: absolute; left: 12px; top: 712px; }
  .badge-text {
    position: absolute; left: 12px; top: 734px; width: 150px;
    text-align: center; font-family: "Noto Serif JP", serif; font-weight: 900;
    font-size: 38px; line-height: 1.15;
  }
  .ribbon {
    position: absolute; left: 150px; top: 795px; width: 300px; height: 46px;
    background: var(--ribbon); color: #fff; font-family: "Noto Serif JP", serif;
    font-weight: 900; font-size: 30px; line-height: 46px; text-align: center;
    clip-path: polygon(0 0, 100% 0, 94% 50%, 100% 100%, 0 100%);
  }
  .gifts { position: absolute; left: 50px; top: 862px; margin: 0; padding: 0; list-style: none; font-weight: 700; font-size: 22px; line-height: 1.5; }
  .gifts li { margin-bottom: 12px; white-space: nowrap; }

  .author { position: absolute; left: 480px; top: 942px; width: 260px; text-align: center; }
  .author-role { font-size: 16px; font-weight: 500; margin: 0; white-space: nowrap; }
  .author-name { font-size: 34px; font-weight: 700; margin: 2px 0 0; letter-spacing: 2px; }

  .notice {
    position: absolute; left: 40px; top: 1065px; margin: 0;
    font-weight: 700; font-size: 36px; line-height: 1.45; white-space: nowrap;
  }
  .notice span { display: block; padding-left: 36px; }
</style>
</head>
<body>
<div class="cover">
  <h1>
    <span class="title title-line1">帳簿が<span class="emph">苦手な</span></span>
    <span class="title title-line2">店主のための</span>
    <span class="title title-main">「街角で商売」</span>
  </h1>
  <svg class="sweat" width="36" height="50" viewBox="0 0 40 56" aria-hidden="true">
    <path d="M20 2 C28 18 36 28 36 38 A16 16 0 0 1 4 38 C4 28 12 18 20 2 Z" fill="var(--drop)"/>
  </svg>

  <div class="subtitle">
    <p><span class="key">小さな会社</span>や</p>
    <p><span class="key">個人事業</span>でもできる!</p>
  </div>

  <div class="portrait" role="img" aria-label="著者似顔絵のイラスト(スーツ姿の女性が左を指さす)"></div>

  <svg class="badge" width="150" height="150" viewBox="0 0 160 160" aria-hidden="true">
    <defs>
      <radialGradient id="gold" cx="40%" cy="35%" r="70%">
        <stop offset="0" stop-color="var(--gold-light)"/>
        <stop offset="1" stop-color="var(--gold-dark)"/>
      </radialGradient>
    </defs>
    <circle cx="80" cy="80" r="76" fill="url(#gold)"/>
    <circle cx="80" cy="80" r="66" fill="none" stroke="#fff6d0" stroke-width="2"/>
  </svg>
  <div class="badge-text">読者<br>限定</div>
  <div class="ribbon">プレゼント付</div>

  <ul class="gifts">
    <li>●思わずポチッと押したくなる!<br>【段階別 キャッチコピーの作り方】</li>
    <li>●真似するだけでOK!<br>【ランディングページのテンプレート】</li>
  </ul>

  <div class="author">
    <p class="author-role">WEB集客のしくみ作りの専門家</p>
    <p class="author-name">森田 サキ</p>
  </div>

  <p class="notice">※この本を読むまでは<span>ホームページは作らないでください。</span></p>
</div>
</body>
</html>
```